Webshop for baby shoes need new design

We are an innovative company selling a one of a kind product on a market with tough competition. We are looking to step up our business and need a new design for our shop.

We are looking for recognition as well as originality. The customer must immediately be able to identify navigation, shopping cart, buy buttons etc. We want warm welcoming colors, but not too strong as to not draw attention away from the products. Retro might be interesting, if "done right".

Suggested color palette: http://huepalettemaker.example/#7k29WbQx3p8r5

We have a logo (attached), but if you have a better idea we might go for that instead. Also, a couple of product images are attached for you to use in the design.

What we do NOT want is a shop that looks like a free template (vendaForge etc). Also, while we are selling baby shoes, we don't want to use the very worn our baby pink/blue scheme, so stay clear of this, thanks.
Updates

We suggest that you use this palette, or similar: http://huepalettemaker.example/#7k29WbQx3p8r5

Project Deadline Extended
Reason: We feel that we are getting closer to finding a design that we like, but there is still a bit to go. Also we want to give the chance to any late starters to show their idea. The competition is still open.

Target Market(s)

babies and their parents

Industry/Entity Type

Shopping

Requirements
Must have
• The usual webshop elements
- shopping cart
- product listing
- product page
- buy buttons
Nice to have
• - large footer area for links, info and function (see trindel.example for an example)
- some kind of product navigation/filter (left, top or right)
- place for promotion banners

```html
<!DOCTYPE html>
<html lang="en">
<head>
<meta charset="utf-8">
<title>Tindlewick Baby Store</title>
<link rel="stylesheet" href="https://fonts.googleapis.com/css2?family=Open+Sans:wght@400;600;700&family=Dancing+Script:wght@400;600&display=swap">
<style>
  :root {
    --sand: #E5CDA4;
    --sand-light: #FBE5DD;
    --berry: #AE3346;
    --orange: #D9622A;
    --teal: #63A99A;
    --teal-text: #4FA08F;
    --page: #EDEDED;
    --card: #F4F4F4;
    --brown: #8A5A2B;
    --ink: #4A4442;
    --grey-text: #555;
    --white: #FFFFFF;
    --ui: "Open Sans", Arial, sans-serif;
    --script: "Dancing Script", cursive;
  }
  * { box-sizing: border-box; margin: 0; padding: 0; }
  html, body { width: 900px; height: 1200px; overflow: hidden; }
  body { background: var(--page); font-family: var(--ui); position: relative; }
  .abs { position: absolute; }

  .site-header { left: 0; top: 0; width: 900px; height: 103px; background: var(--sand); }
  .brand { left: 36px; top: 32px; display: flex; align-items: center; gap: 10px; }
  .brand-mark { width: 58px; height: 58px; background: var(--brown); border-radius: 6px; }
  .brand-name { font-family: var(--ui); font-weight: 700; font-size: 40px; color: var(--brown); letter-spacing: 1px; }
  .account { right: 30px; top: 70px; font-size: 16px; color: var(--grey-text); display: flex; }
  .account span { padding: 0 8px; }
  .account span + span { border-left: 1px solid var(--grey-text); }

  .main-nav { left: 0; top: 103px; width: 900px; height: 47px; background: var(--berry); border-bottom: 3px solid var(--sand); }
  .main-nav a { position: absolute; top: 10px; color: var(--white); font-size: 21px; text-decoration: none; }
  .nav-active-dot { position: absolute; left: 48px; top: 41px; width: 28px; height: 14px; background: var(--sand); border-radius: 14px 14px 0 0; }

  .search-bar { left: 24px; top: 150px; width: 851px; height: 56px; background: var(--sand); border-radius: 0 0 6px 6px; }
  .search-input { position: absolute; left: 24px; top: 11px; width: 650px; height: 36px; background: var(--white); border: 1px solid var(--berry); border-radius: 6px; padding-left: 14px; line-height: 34px; color: #aaa; font-size: 17px; font-style: italic; }
  .search-button { position: absolute; left: 688px; top: 11px; width: 132px; height: 34px; background: var(--berry); color: var(--white); border-radius: 3px; text-align: center; font-size: 23px; line-height: 34px; }

  .hero { left: 24px; top: 216px; width: 573px; height: 259px; background: var(--orange); border-radius: 6px; overflow: hidden; }
  .hero-brand { position: absolute; left: 14px; top: 0; width: 300px; height: 72px; background: var(--sand-light); display: flex; align-items: center; gap: 8px; padding-left: 12px; }
  .hero-brand .brand-mark { width: 48px; height: 48px; }
  .hero-brand .brand-name { font-size: 34px; }
  .hero-title { position: absolute; left: 50px; top: 68px; font-family: var(--script); color: var(--white); font-size: 50px; }
  .hero-arrow { position: absolute; top: 80px; color: var(--white); font-size: 44px; font-weight: 700; }
  .hero-photo { position: absolute; left: 224px; top: 42px; width: 320px; height: 192px; border-radius: 40px 90px 20px 20px; background: linear-gradient(135deg, #2A3A6B 0%, #233058 55%, #E9E9E9 100%); }
  .hero-pager { position: absolute; left: 0; bottom: 0; width: 84px; height: 22px; background: var(--white); clip-path: polygon(0 0, 78% 0, 100% 100%, 0 100%); font-size: 15px; color: var(--teal-text); padding-left: 6px; line-height: 22px; letter-spacing: 1px; }

  .promo { width: 271px; background: var(--berry); border-radius: 6px; color: var(--white); font-family: var(--script); overflow: hidden; }
  .promo-big { font-size: 44px; text-align: center; line-height: 82px; }
  .promo-small { font-family: var(--ui); font-style: italic; font-size: 22px; position: absolute; }
  .promo-script { position: absolute; font-size: 54px; }

  .section-title { left: 24px; width: 604px; height: 38px; background: var(--sand); border-radius: 6px; color: var(--berry); font-size: 32px; padding-left: 10px; line-height: 38px; }
  .product-row { left: 24px; width: 604px; height: 200px; background: var(--card); border: 1px solid var(--sand); display: grid; grid-template-columns: repeat(4, 1fr); padding: 14px 12px 6px; }
  .product { position: relative; padding: 0 6px; }
  .product + .product { border-left: 1px solid #777; }
  .product-photo { width: 92px; height: 72px; margin: 10px auto 0; border-radius: 30px 40px 8px 8px; }
  .product-desc { margin-top: 20px; font-size: 8px; line-height: 10px; color: var(--teal-text); }
  .product-price { font-family: var(--script); color: var(--berry); font-size: 22px; margin-top: 4px; padding-left: 10px; }
  .view-button { position: absolute; right: 4px; bottom: 4px; width: 62px; height: 24px; background: var(--berry); color: var(--white); font-size: 16px; text-align: center; line-height: 24px; border-radius: 2px; }
  .row-arrow { position: absolute; width: 22px; height: 44px; background: var(--berry); color: var(--white); font-size: 22px; line-height: 44px; font-weight: 700; }
  .row-arrow.left { left: -1px; border-radius: 0 22px 22px 0; padding-left: 3px; }
  .row-arrow.right { right: -1px; border-radius: 22px 0 0 22px; padding-left: 6px; }
  .tone-navy { background: linear-gradient(135deg, #2B3B6C, #E27A3C 60%, #ECECEC); }
  .tone-cream { background: linear-gradient(135deg, #F3EEDD, #E6DDC3); }
  .tone-teal { background: linear-gradient(135deg, #2E6478, #1F4E60 70%, #E8E8E8); }
  .tone-blue { background: linear-gradient(135deg, #2D3F73, #7FA7D6 70%, #E8E8E8); }

  .girls-promo { left: 638px; top: 486px; width: 237px; height: 131px; background: var(--teal); border-radius: 6px; color: var(--white); }

  .cart { left: 638px; top: 635px; width: 237px; height: 228px; background: var(--sand); border-radius: 6px; overflow: hidden; }
  .cart-head { height: 39px; background: var(--berry); color: var(--white); font-size: 24px; text-align: center; line-height: 39px; }
  .cart-line { position: absolute; left: 12px; width: 200px; display: flex; justify-content: space-between; color: var(--berry); font-size: 16px; }
  .cart-button { position: absolute; left: 13px; height: 24px; background: var(--berry); color: var(--white); font-weight: 700; font-size: 15px; line-height: 24px; padding: 0 12px; border-radius: 3px; }

  .footer-col { font-size: 13px; color: var(--teal-text); line-height: 16px; }
  .footer-title { color: var(--berry); font-size: 17px; line-height: 22px; }
  .footer-links { border-left: 1px solid var(--teal-text); padding-left: 3px; margin-left: 5px; margin-top: 4px; }
  .social { display: flex; gap: 4px; margin-top: 4px; }
  .social span { width: 26px; height: 25px; background: #3A5A98; border-radius: 2px; }
  .copyright { left: 30px; top: 1168px; width: 844px; height: 32px; background: var(--ink); color: var(--white); font-size: 11px; text-align: center; line-height: 32px; }
</style>
</head>
<body>

<header class="site-header abs">
  <div class="brand abs"><span class="brand-mark"></span><span class="brand-name">Tindlewick</span></div>
  <div class="account abs"><span>Sign in</span><span>Log in</span></div>
</header>

<nav class="main-nav abs">
  <a href="#" style="left:35px">Home</a>
  <a href="#" style="left:139px">shopping cart</a>
  <a href="#" style="left:327px">product listing</a>
  <a href="#" style="left:511px">contact us</a>
  <span class="nav-active-dot"></span>
</nav>

<div class="search-bar abs">
  <div class="search-input">Searching here.........</div>
  <div class="search-button">Search</div>
</div>

<section class="hero abs">
  <div class="hero-brand"><span class="brand-mark"></span><span class="brand-name">Tindlewick</span></div>
  <div class="hero-photo" role="img" aria-label="Photo of a navy and orange leather baby boot with a zip"></div>
  <span class="hero-arrow" style="left:10px">&#x2039;</span>
  <span class="hero-arrow" style="right:10px">&#x203A;</span>
  <div class="hero-title">Baby Store</div>
  <div class="hero-pager">12345</div>
</section>

<div class="promo abs" style="left:604px;top:216px;height:82px"><div class="promo-big">Fresh Arrivals</div></div>
<div class="promo abs" style="left:604px;top:304px;height:81px"><div class="promo-big" style="font-size:40px">Off Beat Designs</div></div>
<div class="promo abs" style="left:604px;top:393px;height:82px">
  <span class="promo-small" style="left:6px;top:4px">Best Buy</span>
  <span class="promo-script" style="left:94px;top:2px">for Boys</span>
</div>

<div class="section-title abs" style="top:486px">Boy</div>
<div class="product-row abs" style="top:532px">
  <div class="product"><div class="product-photo tone-navy" role="img" aria-label="Navy and orange baby boot"></div><div class="product-desc">Lorem ipsum dolor sit amet sit orem ipsum dolor sit amet.</div><div class="product-price">$ 350.00</div><div class="view-button">View</div></div>
  <div class="product"><div class="product-photo tone-cream" role="img" aria-label="Cream leather baby shoe"></div><div class="product-desc">Lorem ipsum dolor sit amet sit orem ipsum dolor sit amet.</div><div class="product-price">$ 350.00</div><div class="view-button">View</div></div>
  <div class="product"><div class="product-photo tone-teal" role="img" aria-label="Teal strap baby shoe"></div><div class="product-desc">Lorem ipsum dolor sit amet sit orem ipsum dolor sit amet.</div><div class="product-price">$ 350.00</div><div class="view-button">View</div></div>
  <div class="product"><div class="product-photo tone-blue" role="img" aria-label="Navy and light blue lace-up baby shoe"></div><div class="product-desc">Lorem ipsum dolor sit amet sit orem ipsum dolor sit amet.</div><div class="product-price">$ 350.00</div><div class="view-button">View</div></div>
  <span class="row-arrow left" style="top:0">&#x2039;</span>
  <span class="row-arrow right" style="top:0">&#x203A;</span>
</div>

<div class="section-title abs" style="top:750px">Girl</div>
<div class="product-row abs" style="top:795px">
  <div class="product"><div class="product-photo tone-navy" role="img" aria-label="Navy and orange baby boot"></div><div class="product-desc">Lorem ipsum dolor sit amet sit orem ipsum dolor sit amet.</div><div class="product-price">$ 350.00</div><div class="view-button">View</div></div>
  <div class="product"><div class="product-photo tone-cream" role="img" aria-label="Cream leather baby shoe"></div><div class="product-desc">Lorem ipsum dolor sit amet sit orem ipsum dolor sit amet.</div><div class="product-price">$ 350.00</div><div class="view-button">View</div></div>
  <div class="product"><div class="product-photo tone-teal" role="img" aria-label="Teal strap baby shoe"></div><div class="product-desc">Lorem ipsum dolor sit amet sit orem ipsum dolor sit amet.</div><div class="product-price">$ 350.00</div><div class="view-button">View</div></div>
  <div class="product"><div class="product-photo tone-blue" role="img" aria-label="Navy and light blue lace-up baby shoe"></div><div class="product-desc">Lorem ipsum dolor sit amet sit orem ipsum dolor sit amet.</div><div class="product-price">$ 350.00</div><div class="view-button">View</div></div>
  <span class="row-arrow left" style="top:0">&#x2039;</span>
  <span class="row-arrow right" style="top:0">&#x203A;</span>
</div>

<div class="girls-promo abs">
  <span class="promo-small" style="left:12px;top:12px;font-family:var(--ui);font-style:italic;font-size:26px">Best Buy</span>
  <span class="promo-script abs" style="left:16px;top:40px;font-family:var(--script);font-size:66px">for Girls</span>
</div>

<aside class="cart abs">
  <div class="cart-head">My Cart</div>
  <div class="cart-line" style="top:76px"><span>Shopping</span><span>$0.00</span></div>
  <div class="cart-line" style="top:116px"><span>Total</span><span>$0.00</span></div>
  <div class="cart-button" style="top:153px">Cart</div>
  <div class="cart-button" style="top:189px">Check out</div>
</aside>

<footer>
  <div class="footer-col abs" style="left:79px;top:1015px">
    <div class="footer-title">Links</div>
    <div class="footer-links">kinfold.example<br>mailpost.example<br>letterbay.example<br>kinfold.example</div>
  </div>
  <div class="footer-col abs" style="left:326px;top:1014px">
    Home<br>shopping cart<br>product listing<br>product page<br>buy buttons<br><span style="display:block;margin-top:4px">contact us</span>
  </div>
  <div class="footer-col abs" style="left:641px;top:1015px">
    <div class="footer-title">Follow</div>
    <div class="social"><span aria-label="Social profile one"></span><span aria-label="Social profile two"></span></div>
  </div>
  <div class="copyright abs">Copyright@2012 By tindlewick.example.All Rights Reserved.</div>
</footer>

</body>
</html>
```